Dietitian/Nutritionist seeks trifold marketing brochure

We need a trifold brochure for marketing to patients within a doctors surgery. This will be a source of information for prospective patients, what they can expect and how to contact us. The brochure needs to have some key information such as a brief description of the services available, fees, locations of clinics and contact information. Our current brochure has been uploaded which has the information you need to complete this project. The files you provide will allow us to edit the information at a later date as pricing and services change.

Target Market(s)

Patients who have been referred to see a dietitian/nutritionist and people who are considering seeing a dietitian/nutritionist but haven't decided

Industry/Entity Type

Dietician

Font styles to use
Serif

Colors

Designer to choose colors to be used in the design.

Requirements
Must have
• My logo
• Verified clinical mealwise logo
• My website address and contact details
• Most of the information that is in my current brochure
• Locations/names of the four clinics
Nice to have
• Images that promote cooking, health and wellbeing

```html
<!DOCTYPE html>
<html lang="en">
<head>
<meta charset="utf-8">
<title>Kestrel Nutrition &amp; Dietetics – Trifold Brochure</title>
<link rel="stylesheet" href="https://fonts.googleapis.com/css2?family=Alegreya:wght@400;700&family=Alegreya+Sans:wght@700&display=swap">
<style>
:root{
  --stage:#b9b9b9;
  --orange-hot:#f07a22;
  --orange-mid:#c8561a;
  --orange-deep:#6e2a0c;
  --ink:#ffffff;
  --ink-soft:#fbe9dc;
  --brand:#1f5aa6;
  --badge:#ef7b22;
}
*{margin:0;padding:0;box-sizing:border-box}
html,body{width:1061px;height:1200px;overflow:hidden;background:var(--stage)}
body{position:relative;font-family:"Alegreya",Georgia,serif;color:var(--ink)}
.spread{position:absolute;left:124px;width:822px;height:575px;overflow:hidden;
  background:radial-gradient(ellipse 70% 80% at 50% 50%,var(--orange-hot) 0%,var(--orange-mid) 55%,var(--orange-deep) 100%)}
.spread--inside{top:14px}
.spread--outside{top:610px}
.fold{position:absolute;top:0;bottom:0;width:1px;background:rgba(0,0,0,.12)}
.abs{position:absolute}
.body-copy{font-size:13px;line-height:21.6px;letter-spacing:-.2px}
.justify{text-align:justify}
h3{font-size:14px;font-weight:700;line-height:20px}
h2{font-size:17px;font-weight:700;line-height:22px}
.logo{position:absolute;background:#fff;box-shadow:0 1px 3px rgba(0,0,0,.35);display:flex;align-items:center;justify-content:center;gap:6px;color:var(--brand);font-weight:700;white-space:nowrap}
.logo .dot{border-radius:50%;background:var(--brand);flex:none}
.badge{position:absolute;background:var(--badge);border:1px solid rgba(255,255,255,.4);display:flex;align-items:center;justify-content:space-between;font-family:"Alegreya",Georgia,serif;color:#fff}
.badge .seal{border-radius:50%;background:#fff;flex:none}
.photo{position:absolute;background:#fff;box-shadow:0 1px 3px rgba(0,0,0,.4)}
.photo .fill{position:absolute;inset:3px}
.roundel{position:absolute;border-radius:50%;background:#fff;box-shadow:0 1px 4px rgba(0,0,0,.4)}
.roundel .fill{position:absolute;inset:4px;border-radius:50%}
.ticks{list-style:none}
.ticks li{position:relative;padding-left:27px;font-size:15px;line-height:16px;margin-bottom:16px}
.ticks svg{position:absolute;left:0;top:2px}
.center{text-align:center}
.promise{font-size:17px;line-height:23px}
.tagline{font-family:"Alegreya Sans",Arial,sans-serif;font-weight:700;font-size:22px;line-height:20px;text-align:right}
.contact{font-size:17px;line-height:24px}
.contact strong{font-size:18px}
</style>
</head>
<body>

<!-- Inside spread -->
<section class="spread spread--inside">
  <div class="fold" style="left:410px"></div>

  <div class="abs body-copy justify" style="left:52px;top:44px;width:332px">
    Verified clinical mealwise (VCMs) are university trained experts in food and nutrition, they are able to translate the latest scientific evidence into sensible and practical advice. Dietitians differ from nutritionists as they have specific training in clinical environments such as hospitals. This training allows a dietitian to interpret blood tests, understand any food and medication interactions, and communicate with other health professionals involved in your care.
  </div>

  <div class="abs body-copy" style="left:52px;top:238px;width:340px">
    <h3>Seeing a dietitian for the first time</h3>
    involves working with you to develop, strategies and goals to improve your health. Follow up visits are recommended to monitor your progress and may include more measurements and new strategies to help YOU realise your goals. Every person is unique and I can.
  </div>

  <div class="photo" style="left:48px;top:394px;width:106px;height:70px">
    <div class="fill" role="img" aria-label="Photo of a green and a red apple" style="background:linear-gradient(90deg,#7dbb2a 0 48%,#c3262a 52% 100%)"></div>
  </div>

  <div class="abs" style="left:165px;top:390px;width:230px;font-size:12px;line-height:19px">
    <strong>Locations :</strong><br>
    Elmridge Medical Centre Hillcrest - Fridays<br>
    Brookvale Medical - Wednesdays<br>
    Harbour Health Riverside – Thursdays<br>
    Oakden Doctors Surgery – Approximately<br>every 4 weeks
  </div>

  <div class="logo" style="left:49px;top:517px;width:102px;height:38px;font-size:11px">
    <span class="dot" style="width:10px;height:10px"></span>Kestrel
  </div>
  <div class="badge" style="left:281px;top:514px;width:100px;height:47px;padding:0 5px 0 6px;font-size:8px;line-height:9px">
    <span>Verified<br>clinical<br>mealwise</span><span class="seal" style="width:37px;height:37px"></span>
  </div>

  <div class="logo" style="left:518px;top:27px;width:154px;height:62px;font-size:19px">
    <span class="dot" style="width:16px;height:16px"></span>Kestrel
  </div>

  <div class="abs body-copy" style="left:433px;top:96px;width:330px;line-height:23.5px">
    <h2>Fees:</h2>
    <h3>Chronic Disease Management Plans</h3>
    If your Doctor has referred you with a Chronic Disease Management Plan to assist in the ongoing management of your health condition you are eligible for a rebate of $52.95 from
    <h3 style="margin-top:22px">Medicare.</h3>
    All Fees are payable on the day<br>
    Private Patients<br>
    Initial Consultation &nbsp;(60mins) $120<br>
    Follow up Consultation (30mins) $65
    <h3 style="margin-top:22px">Private Health Funds</h3>
    Rebates are available through most private health funds but rates vary depending on your level of cover. Check with your fund directly to find out more.
    <p style="margin-top:23px">Payment is required on the day of your consultation.</p>
  </div>
</section>

<!-- Outside spread -->
<section class="spread spread--outside">
  <div class="fold" style="left:274px"></div>
  <div class="fold" style="left:548px"></div>

  <div class="roundel" style="left:106px;top:23px;width:70px;height:70px">
    <div class="fill" role="img" aria-label="Photo of raspberries with a leaf" style="background:radial-gradient(circle at 40% 55%,#c8183a,#e85a6a 60%,#6da83a 100%)"></div>
  </div>
  <div class="abs" style="left:41px;top:112px;width:225px">
    <h3 style="font-size:15px;line-height:16px">Verified clinical mealwise</h3>
    <p style="font-size:14px;line-height:16px">can assist you with:</p>
  </div>
  <ul class="ticks abs" style="left:15px;top:162px;width:250px">
    <li><svg width="20" height="16" viewBox="0 0 20 16"><path d="M2 9l5 5L18 2" fill="none" stroke="#fff" stroke-width="3"/></svg>Diabetes – Impaired Glucose Tolerance, Type 1 &amp; 2 Diabetes,Gestational Diabetes</li>
    <li><svg width="20" height="16" viewBox="0 0 20 16"><path d="M2 9l5 5L18 2" fill="none" stroke="#fff" stroke-width="3"/></svg>Digestive Health– Irritable Bowel Syndrome, Coeliac Disease, Diverticular Disease</li>
    <li><svg width="20" height="16" viewBox="0 0 20 16"><path d="M2 9l5 5L18 2" fill="none" stroke="#fff" stroke-width="3"/></svg>Gastric banding and other surgical methods of weight loss</li>
    <li><svg width="20" height="16" viewBox="0 0 20 16"><path d="M2 9l5 5L18 2" fill="none" stroke="#fff" stroke-width="3"/></svg>Cardiovascular - High cholesterol, High Blood Pressure, Risk Reduction</li>
    <li><svg width="20" height="16" viewBox="0 0 20 16"><path d="M2 9l5 5L18 2" fill="none" stroke="#fff" stroke-width="3"/></svg>Weight Management – loss/gain and support</li>
    <li><svg width="20" height="16" viewBox="0 0 20 16"><path d="M2 9l5 5L18 2" fill="none" stroke="#fff" stroke-width="3"/></svg>General Healthy Eating &amp; Nutrition</li>
  </ul>
  <div class="logo" style="left:99px;top:499px;width:83px;height:33px;font-size:10px">
    <span class="dot" style="width:9px;height:9px"></span>Kestrel
  </div>

  <div class="roundel" style="left:373px;top:23px;width:82px;height:82px">
    <div class="fill" role="img" aria-label="Photo of fresh fruit with a stethoscope" style="background:radial-gradient(circle at 50% 50%,#f6a623,#e8791d 50%,#8fb64a 100%)"></div>
  </div>
  <p class="abs center promise" style="left:290px;top:113px;width:242px">Helping you to meet your individual nutrition goals with an emphasis on practical skills, eryday foods, and providing you.</p>
  <p class="abs tagline" style="left:300px;top:270px;width:96px">with up<br>to date<br>advice.</p>
  <div class="photo" style="left:403px;top:275px;width:97px;height:58px">
    <div class="fill" role="img" aria-label="Photo of garlic bulbs and parsley" style="background:radial-gradient(circle at 55% 50%,#efe6d6,#d8ccb4 55%,#f4f4f4 100%)"></div>
  </div>
  <p class="abs center promise" style="left:290px;top:420px;width:242px">We work together to develop personalised eating plans that take</p>
  <div class="logo" style="left:373px;top:500px;width:83px;height:33px;font-size:10px">
    <span class="dot" style="width:9px;height:9px"></span>Kestrel
  </div>

  <div class="logo" style="left:600px;top:21px;width:174px;height:70px;font-size:22px">
    <span class="dot" style="width:18px;height:18px"></span>Kestrel
  </div>
  <div class="abs center contact" style="left:552px;top:190px;width:266px">
    <strong>Daniel Whitcombe</strong><br>
    <strong>0400 555 218</strong><br>
    daniel.w.nutrition@example.com
    <p style="margin-top:24px">www.kestreldietitian.example<br>Fax: 6300 0147<br>Verified clinical mealwise &amp; Chef</p>
  </div>
  <div class="badge" style="left:610px;top:477px;width:148px;height:70px;padding:0 8px 0 8px;font-size:12px;line-height:13px">
    <span>Verified<br>clinical<br>mealwise</span><span class="seal" style="width:56px;height:56px"></span>
  </div>
</section>

</body>
</html>
```